Records Management Company Revamp

We are looking to revamp our web presence, and need a catchy design that helps us to get noticed! We would like the website to be in wordpress. the main requirements are a home page, a landing page template for SEO / PPC, and then a few other pages that can be reused throughout the website.

We are happy to supply content / video etc.

Number of Pages Required

3 page

Font styles to use
Other font styles liked:
• Find fonts listed in attached branding document

Requirements
Must have
• Home page as well as sub pages according to their colours. Need to use colours and fonts set out in branding guide. Attached are examples of home page and sub pages.
Nice to have
• We have uploaded some very basic ideas we have of how we wish the website to look, but looking to have it more professional and fit together. Please see uploaded items.

```html
<!DOCTYPE html>
<html lang="en">
<head>
<meta charset="utf-8">
<title>Keepwell Storage – Home</title>
<link href="https://fonts.googleapis.com/css2?family=Oswald:wght@400;500&family=Arimo:wght@400;700&display=swap" rel="stylesheet">
<style>
:root{
  --blue:#2a7fc9;--blue-dark:#1d5f9e;--orange:#f28c1e;--red:#c8102e;--green:#7ab342;
  --sky:#7fb2d6;--grey:#ebebeb;--ink:#222;--text:#444;--footer:#1b1b1b;--white:#fff;
}
*{box-sizing:border-box;margin:0;padding:0}
html,body{width:1200px;height:3226px;overflow:hidden}
body{position:relative;background:var(--white);font-family:"Arimo",Arial,sans-serif;color:var(--text)}
.abs{position:absolute}
h1,h2,h3,.heading{font-family:"Oswald",Arial,sans-serif;font-weight:500;text-transform:uppercase}
/* header */
.site-header{left:0;top:0;width:1200px;height:129px;background:linear-gradient(90deg,#1f6fb5,#3b8fd6 60%,#2a7fc9);z-index:3}
.brand{left:78px;top:36px;display:flex;align-items:center;gap:12px;color:#fff;font-family:"Oswald",sans-serif;font-size:38px;font-weight:500;text-transform:uppercase;letter-spacing:1px}
.brand-square{width:34px;height:34px;background:#fff}
.main-nav{left:337px;top:86px;display:flex;gap:36px;font-family:"Arimo",sans-serif;font-weight:700;font-size:14px;color:#fff;text-transform:uppercase}
.cart{left:1088px;top:26px;width:36px;height:36px;border-radius:50%;background:var(--orange)}
/* hero */
.hero-photo{left:0;top:129px;width:1200px;height:590px;background:linear-gradient(160deg,#6b4a35 0%,#9c7a5c 35%,#4a5a48 70%,#3b3b35 100%)}
.hero-slope{left:0;top:560px;width:1200px;height:170px}
.hero-title{left:76px;top:318px;color:#fff;font-size:38px;line-height:1.15;font-weight:400}
.hero-title span{display:block;font-size:64px;font-weight:500}
.dots{left:76px;top:540px;display:flex;gap:10px}
.dots i{width:11px;height:11px;border-radius:50%;background:#fff}
.dots i:first-child{background:var(--orange)}
.contact-form{left:795px;top:176px;width:330px;height:409px;background:var(--blue);border-radius:6px;padding:18px 22px}
.contact-form h2{color:#fff;text-align:center;font-size:20px;line-height:1.35;font-weight:400;margin-bottom:14px}
.field{height:40px;background:#fff;border-radius:20px;margin-bottom:10px;padding:0 20px;font-size:13px;line-height:40px;color:#333}
.field.message{height:88px;border-radius:16px;line-height:1;padding-top:14px}
.btn{display:block;background:var(--orange);color:#fff;text-align:center;border-radius:26px;font-family:"Oswald",sans-serif;text-transform:uppercase;font-weight:500}
.contact-form .btn{height:50px;line-height:50px;font-size:22px;margin-top:14px}
/* service cards */
.service{top:619px;width:240px;height:258px;border-radius:8px;padding:10px}
.service .thumb{height:196px;border-radius:6px}
.service h3{color:#fff;text-align:center;font-size:22px;margin-top:12px;font-weight:500}
/* sections */
.band-grey{background:var(--grey)}
.section-title{font-size:38px;color:var(--ink)}
.body-copy{font-size:14px;line-height:26.5px;color:#333}
/* team */
.member{width:331px;height:124px;border:1px solid #d6d6d6;border-radius:10px;background:#fff;padding:14px 16px;display:flex;gap:14px}
.member .avatar{width:106px;height:94px;flex:none;border-radius:2px}
.member h3{color:var(--blue);font-size:16px;margin-bottom:6px}
.member p{font-size:12.5px;line-height:19px;color:#444}
.cta{left:795px;top:1359px;width:330px;height:330px;background:var(--blue);border-radius:6px;padding:26px 26px;text-align:center;color:#fff}
.cta h2{font-size:38px;line-height:1.15;font-weight:500}
.cta p{font-size:14px;line-height:22px;margin-top:12px}
.cta .btn{height:50px;line-height:50px;font-size:24px;margin-top:22px}
/* why */
.why{top:1890px;width:320px;text-align:center}
.why svg{display:block;margin:0 auto 14px}
.why h3{color:var(--blue);font-size:24px;margin-bottom:14px}
.why p{font-size:14px;line-height:25px;color:#444}
.badge{top:2342px;height:46px;border-radius:23px;background:#e0e0e0}
/* testimonials / areas */
.quote{left:76px;top:2606px;width:310px;font-size:17px;line-height:29px;color:#555}
.author-photo{left:76px;top:2778px;width:84px;height:84px;border-radius:50%}
.author{left:180px;top:2808px;color:var(--red);font-size:22px}
.area{top:2615px;width:220px}
.area .ring{width:86px;height:86px;border:2px solid #666;border-radius:50%;display:flex;align-items:center;justify-content:center}
.area h3{color:var(--blue);font-size:24px;margin:18px 0 6px}
.area p{font-size:14.5px;line-height:23px;color:#444}
/* footer */
.site-footer{left:0;top:2924px;width:1200px;height:302px;background:var(--footer);color:#ccc}
.footer-brand{left:78px;top:54px;display:flex;gap:10px;align-items:center;font-family:"Oswald",sans-serif;font-size:30px;text-transform:uppercase;color:#ddd}
.footer-brand i{width:26px;height:26px;background:#ddd}
.legal{left:78px;top:172px;font-size:11.5px;line-height:26px;color:#aaa}
.social{left:78px;top:238px;display:flex;gap:16px}
.social i{width:22px;height:22px;border-radius:50%;background:#888}
.fcol{top:56px}
.fcol h4{font-family:"Oswald",sans-serif;font-weight:500;text-transform:uppercase;color:#fff;font-size:22px;margin-bottom:12px}
.fcol li{list-style:none;font-size:14.5px;line-height:30.5px;color:#ddd}
.office{color:var(--orange);font-weight:700;text-transform:uppercase}
.contact-line{display:flex;align-items:center;gap:16px}
.scale-note{left:1148px;top:3130px;font-size:13px;color:#ddd}
</style>
</head>
<body>

<header class="site-header abs">
  <div class="brand abs"><span class="brand-square"></span>Keepwell Storage</div>
  <nav class="main-nav abs"><span>Home</span><span>Offsite Storage</span><span>Document Shredding</span><span>Digitisation</span><span>Archive Supplies</span><span>Contactus</span></nav>
  <div class="cart abs"><svg width="36" height="36" viewBox="0 0 36 36"><path d="M10 12h3l2 9h9l2-6H14" fill="none" stroke="#fff" stroke-width="2"/><circle cx="16" cy="25" r="1.6" fill="#fff"/><circle cx="23" cy="25" r="1.6" fill="#fff"/></svg></div>
</header>

<div class="hero-photo abs" role="img" aria-label="Warehouse interior with shelves of archive boxes and a staff member on a stair"></div>
<svg class="hero-slope abs" viewBox="0 0 1200 170" preserveAspectRatio="none"><polygon points="0,170 1200,80 1200,170" fill="#fff"/></svg>
<h1 class="hero-title abs">Welcome to<span>Keepwell Storage</span></h1>
<div class="dots abs"><i></i><i></i><i></i><i></i></div>

<form class="contact-form abs">
  <h2>Receive any of your suggestion via email</h2>
  <div class="field">Name</div>
  <div class="field">Email Addresss</div>
  <div class="field">Subject</div>
  <div class="field message">Message</div>
  <span class="btn">Send Message</span>
</form>

<div class="service abs" style="left:75px;background:var(--red)"><div class="thumb" role="img" aria-label="Open filing drawer with red tabbed folders" style="background:linear-gradient(160deg,#e6e6e6,#b9b9b9)"></div><h3>Offsite Storage</h3></div>
<div class="service abs" style="left:346px;background:var(--green)"><div class="thumb" role="img" aria-label="Hands holding shredded paper" style="background:linear-gradient(160deg,#5a5a5a,#cfcfcf)"></div><h3>Document Shredding</h3></div>
<div class="service abs" style="left:617px;background:var(--orange)"><div class="thumb" role="img" aria-label="Document being placed on a scanner" style="background:linear-gradient(160deg,#d8b79a,#eef0f2)"></div><h3>Digitisation</h3></div>
<div class="service abs" style="left:888px;background:var(--sky)"><div class="thumb" role="img" aria-label="Stacked cardboard archive boxes" style="background:linear-gradient(160deg,#a87a4f,#6d4a2c)"></div><h3>Archive Supplies</h3></div>

<section class="band-grey abs" style="left:0;top:925px;width:1200px;height:380px"></section>
<h2 class="section-title abs" style="left:76px;top:1004px">How offsite storage works</h2>
<p class="body-copy abs" style="left:76px;top:1072px;width:700px">We deliver boxes and Barcodes if you need them, we get you started with all the essentials to prepare your archives. We pickup your documents when your boxes are ready, let us know and we'll come by and collect your documents. We Store Your Documents You documents are stored in our secure purpose built facility in Harbourview/Eastfield. We Retrieve &amp; Deliver Your Documents When you need your documents, just call or email us and we'll get them to you! We Can Securely Destroy We can work with you on determining which documents can be securely destroyed and do this for you!</p>
<div class="abs" role="img" aria-label="Open archive box filled with files" style="left:826px;top:990px;width:210px;height:290px;background:linear-gradient(170deg,#f3f3f3,#c9c9c9);border-radius:4px"></div>

<h2 class="section-title abs" style="left:76px;top:1350px">Team</h2>
<div class="member abs" style="left:75px;top:1415px"><div class="avatar" role="img" aria-label="Team member portrait" style="background:linear-gradient(#8a9bb0,#3c4a5c)"></div><div><h3>Name Heading</h3><p>Lorem, et posuere risus lacinia sit ametcurabitur eu iaculis ero sit amet</p></div></div>
<div class="member abs" style="left:434px;top:1415px"><div class="avatar" role="img" aria-label="Team member portrait" style="background:linear-gradient(#f1e2c6,#c9a36e)"></div><div><h3>Name Heading</h3><p>Lorem, et posuere risus lacinia sit ametcurabitur eu iaculis ero sit amet</p></div></div>
<div class="member abs" style="left:75px;top:1557px"><div class="avatar" role="img" aria-label="Team member portrait" style="background:linear-gradient(#e9d8cf,#5a3328)"></div><div><h3>Name Heading</h3><p>Lorem, et posuere risus lacinia sit ametcurabitur eu iaculis ero sit amet</p></div></div>
<div class="member abs" style="left:434px;top:1557px"><div class="avatar" role="img" aria-label="Team member portrait" style="background:linear-gradient(#d9d9d9,#2a2e36)"></div><div><h3>Name Heading</h3><p>Lorem, et posuere risus lacinia sit ametcurabitur eu iaculis ero sit amet</p></div></div>

<aside class="cta abs"><h2>Maecenas rhoncus lorem nec</h2><p>Sed mollis sollicitudin lorem, et posuere risus lacinia sit amet. Curabitur eu iaculis eros. Nulla sit amet arcu eget justo consequat rutrum</p><span class="btn">Call us now</span></aside>

<section class="band-grey abs" style="left:0;top:1746px;width:1200px;height:430px;clip-path:polygon(0 0,100% 0,100% 88%,0 100%)"></section>
<h2 class="section-title abs" style="left:0;top:1792px;width:1200px;text-align:center">Why choose us</h2>
<div class="why abs" style="left:81px"><svg width="70" height="50" viewBox="0 0 70 50"><rect x="10" y="4" width="50" height="34" rx="3" fill="none" stroke="var(--red)" stroke-width="4"/><rect x="2" y="40" width="66" height="6" rx="2" fill="var(--red)"/></svg><h3>Sed mollis sollicitudin</h3><p>Lorem, et posuere risus lacinia sit ametcurabitur eu iaculis eros. Nulla sit amet arcu eget justo consequat rutrum. Vivamus varius vitae libero sed ultricies</p></div>
<div class="why abs" style="left:440px"><svg width="70" height="50" viewBox="0 0 70 50"><path d="M24 2h16l10 10v36H24z" fill="var(--red)"/><path d="M29 24h16M29 31h16M29 38h16" stroke="#fff" stroke-width="2.5"/></svg><h3>Sed mollis sollicitudin</h3><p>Lorem, et posuere risus lacinia sit ametcurabitur eu iaculis eros. Nulla sit amet arcu eget justo consequat rutrum. Vivamus varius vitae libero sed ultricies</p></div>
<div class="why abs" style="left:800px"><svg width="70" height="50" viewBox="0 0 70 50"><rect x="24" y="2" width="22" height="20" fill="var(--red)"/><rect x="12" y="26" width="22" height="20" fill="var(--red)"/><rect x="36" y="26" width="22" height="20" fill="var(--red)"/></svg><h3>Sed mollis sollicitudin</h3><p>Lorem, et posuere risus lacinia sit ametcurabitur eu iaculis eros. Nulla sit amet arcu eget justo consequat rutrum. Vivamus varius vitae libero sed ultricies</p></div>

<h2 class="section-title abs" style="left:0;top:2258px;width:1200px;text-align:center">Accreditation</h2>
<div class="badge abs" style="left:90px;width:170px"></div>
<div class="badge abs" style="left:298px;width:180px"></div>
<div class="badge abs" style="left:514px;width:170px"></div>
<div class="badge abs" style="left:712px;width:212px"></div>
<div class="badge abs" style="left:966px;width:160px"></div>

<section class="band-grey abs" style="left:0;top:2458px;width:1200px;height:466px;clip-path:polygon(0 8%,100% 0,100% 100%,0 100%)"></section>
<h2 class="section-title abs" style="left:76px;top:2536px">Testimonials</h2>
<p class="quote abs">“ Sed mollis sollicitudin lorem, et posuere risus lacinia sit amet. Curabitur eu iaculis eros. Nulla sit amet arcu eget justo consequat rutrum. Vivamus varius vitae libero sed ultricies..”</p>
<div class="author-photo abs" role="img" aria-label="Client portrait" style="background:linear-gradient(#cfcfcf,#555)"></div>
<h3 class="author abs">Name Heading</h3>

<h2 class="section-title abs" style="left:434px;top:2536px">Areas we service</h2>
<div class="area abs" style="left:434px"><div class="ring"><svg width="40" height="36" viewBox="0 0 40 36"><rect x="3" y="9" width="34" height="24" rx="3" fill="var(--red)"/><rect x="14" y="3" width="12" height="8" fill="none" stroke="var(--red)" stroke-width="3"/></svg></div><h3>Corporate</h3><p>Lorem, et posuere risus lacinia sit ametcurabitur eu iaculis eros. Nulla sit amet arcu eget justo consequat rutrum varius vitae libero sed ultricies</p></div>
<div class="area abs" style="left:669px"><div class="ring"><svg width="40" height="40" viewBox="0 0 40 40"><path d="M4 36V18l16-10 16 10v18z" fill="var(--red)"/><rect x="16" y="24" width="8" height="12" fill="#fff"/><path d="M20 8V2h8" stroke="var(--red)" stroke-width="2" fill="none"/></svg></div><h3>Schools</h3><p>Lorem, et posuere risus lacinia sit ametcurabitur eu iaculis eros. Nulla sit amet arcu eget justo consequat rutrum varius vitae libero sed ultricies</p></div>
<div class="area abs" style="left:905px"><div class="ring"><svg width="30" height="40" viewBox="0 0 30 40"><path d="M15 38C15 38 3 22 3 14a12 12 0 0124 0c0 8-12 24-12 24z" fill="var(--red)"/><circle cx="15" cy="14" r="4.5" fill="#fff"/></svg></div><h3>Soho</h3><p>Lorem, et posuere risus lacinia sit ametcurabitur eu iaculis eros. Nulla sit amet arcu eget justo consequat rutrum varius vitae libero sed ultricies</p></div>

<footer class="site-footer abs">
  <div class="footer-brand abs"><i></i>Keepwell Storage</div>
  <p class="legal abs">Copyright © 2019. Company Name<br>All Rights Reserved.</p>
  <div class="social abs"><i></i><i></i><i></i><i></i><i></i></div>
  <div class="fcol abs" style="left:389px"><h4>Navigation</h4><ul><li>Home</li><li>Offsite Storage</li><li>Document Shredding</li><li>Digitisation</li><li>Archive Supplies</li><li>Contactus</li></ul></div>
  <div class="fcol abs" style="left:654px"><h4>Resources</h4><ul><li>Sed mollis</li><li>Sollicitudin lorem</li><li>Posuere risus</li><li>Lacinia sit amet</li><li>Curabitur eu</li></ul></div>
  <div class="fcol abs" style="left:875px"><h4>Contact Details</h4><ul>
    <li class="office">Head Office - Eastbridge</li>
    <li class="contact-line"><svg width="14" height="14" viewBox="0 0 14 14"><path d="M3 1l3 3-2 2a8 8 0 004 4l2-2 3 3-2 2C5 13 1 9 1 3z" fill="#ddd"/></svg>1300 555 014</li>
    <li class="contact-line"><svg width="14" height="14" viewBox="0 0 14 14"><rect x="1" y="4" width="12" height="9" fill="#ddd"/><rect x="3" y="1" width="8" height="4" fill="none" stroke="#ddd"/></svg>(03) 5550 1842</li>
    <li class="contact-line"><svg width="14" height="14" viewBox="0 0 14 14"><rect x="1" y="3" width="12" height="9" fill="#ddd"/><path d="M1 3l6 5 6-5" stroke="#1b1b1b" fill="none"/></svg>hello@keepwellstorage.example</li>
  </ul></div>
  <span class="scale-note abs">x10</span>
</footer>

</body>
</html>
```